Website Design Needed for Fundhaven-style Site

I need a design for a new website that is similar in concept in some ways to fundhaven.example, but with a completely different market.

On one side, the site allows people to post projects for people to help fund, but where fundhaven.example is focused on "creative" projects, this new site is focused on more serious "business-like" projects.

On the other side, the site allows visitors to help fund projects by pledging money in return for various rewards. In the attached image, ProjectDetailsConcept.png, the sidebar currently does not show the rewards mocked up, but there would need to be rewards listed there similar to what is shown here: http://www.fundhaven.example/projects/tomvel/paper-loop?ref=highlight

The Project Details page will contain all the details for a given project. Note that some details are on different tabs on this page. Also note that the project description could be VERY long in some cases.

IMPORTANT: Although I have attached some concept images, please keep in mind that these are very rough and are mainly to illustrate what sort of content needs to be on the pages. None of the content on these mockup pages is final content.

Feel free to experiment with different layouts and concepts if you think they present the information better.

Pages Needed
1. Front Page - Shows main feature area, sub feature area, main menu, other links, search field and footer

2. Search/Browse Page - Lets users refine a search by clicking category names, locations, sort order, etc. Search results are listed below with next/prev controls and page number controls to navigate the results.

3. Project Details Page - Presents details of a given project. The specific details of the page content are not especially important. It is important that the Project Details Page allows multiple sections or tabs to be displayed though. The content in the sidebar of ProjectDetailsConcept.png is fairly representative of what might go there, especially in the top section of the sidebar. The top section should standout from the bottom section of the sidebar.

Keywords to try to relate in the site design: reliable, progressive, innovative, trustworthy, successful

Note that I do not yet have a logo for this site, but assume it is roughly the size and shape of the placeholder in the attached mockups.
Updates

I did some looking around at existing templates.

There are layout and color schemes in all of these that I like:

http://cms.layoutnook.example/blogsite_48172/ (I quite like this one & it has dynamic)
http://51836.themes.pagebarn.example/
http://shp4.layoutnook.example/widened_27341/ (green with orange/yellow is nice)
http://pics.shp4.layoutnook.example/qx_63518/index.html

Also, please give consideration to the font choice for the site.  If necessary I can use cufon, Sifr or @fontface.

NOTE: I added another file called GreenHeaderMockup.png that is based on one of the website links in my previous update.

I like the body, but not the following aspects:

1. The header area needs some rework.  Maybe just a texture.

2. The project info for the featured project looks out of place.  Not sure where a better place would be, but see what comes to mind for you.

3. The project cards at the bottom are some variations...not sure which one I like the most.  Alternatives?

Feel free to ask questions.

Thanks.

Industry/Entity Type

Business

Requirements
Must have
• There must be a dynamic "Featured Projects" area near the top of the home page. This is similar in concept to the featured apps shown in the top of the Gizmo Apps Market. The set of available projects should somehow rotate or transition to focus on one project at a time while still leaving the others visible, but smaller. See the attached FrontPageConcept1.png image for a rough idea. Of course you are not responsible for coding the dynamic behavior, but you need to prepare the required graphical components to support any dynamic behavior you design.

The Search/Browse page must show a collection of "project cards", each of which contains some basic information about the project and an image. I have attached a file that shows some possible layouts for project cards.

See the attached SearchConcept1.png image for a concept that places all the search controls along the top, and the search results below. The concept shows two wide rows of project cards, but it would also be acceptable to show 4 rows of taller cards as in SearchConcept2.png

See the attached SearchConcept2.png image for a concept that places all the search controls in a sidebar, and the search results next to the sidebar. With this orientation, I think 3 tall project cards per row are all that can fit.

Should not have
• Must not use Flash or any other browser plugin.

```html
<!DOCTYPE html>
<html lang="en">
<head>
<meta charset="utf-8">
<title>Browse Projects – Graphic Design</title>
<link rel="stylesheet" href="https://fonts.googleapis.com/css2?family=Open+Sans:wght@400;600;700&display=swap">
<style>
:root{
  --green:#6cae1c;
  --green-light:#9bd63a;
  --green-dark:#2f6b08;
  --ink:#222;
  --text:#555;
  --line:#d8d8d8;
  --page:#f3f3f3;
  --white:#fff;
  --bar:#1d1d1d;
}
*{box-sizing:border-box;margin:0;padding:0}
html,body{width:1200px;height:2471px;overflow:hidden}
body{font-family:"Open Sans",Arial,sans-serif;color:var(--text);background:var(--page);position:relative}
a{color:inherit;text-decoration:none}

/* header */
.site-header{position:absolute;left:0;top:0;width:1200px;height:130px;background:linear-gradient(180deg,#3f8d0c 0%,#5aa615 55%,#3c8a0a 100%)}
.logo{position:absolute;left:45px;top:44px;font-size:40px;font-weight:700;color:var(--white);letter-spacing:1px}
.account-links{position:absolute;right:50px;top:30px;font-size:14px;color:#e6f6c8}
.account-links span{margin:0 10px}
.utility-links{position:absolute;left:775px;top:74px;display:flex;gap:34px;font-size:16px;color:var(--white)}
.header-social{position:absolute;right:50px;top:76px;display:flex;gap:14px}
.header-social i{width:24px;height:24px;border-radius:4px;background:rgba(255,255,255,.35);display:block}

.main-nav{position:absolute;left:0;top:130px;width:1200px;height:54px;background:linear-gradient(180deg,#2a6506,#1d4a03)}
.main-nav ul{list-style:none;display:flex;height:54px;align-items:center}
.main-nav li{font-size:18px;color:var(--white);margin-left:72px}
.main-nav li.active{margin-left:45px;background:linear-gradient(180deg,#8bc832,#5d9d16);height:54px;line-height:54px;padding:0 32px}
.search-box{position:absolute;left:845px;top:12px;width:305px;height:31px;background:var(--white);border-radius:4px;padding-left:14px;font-size:14px;line-height:31px;color:#666}
.search-box svg{position:absolute;right:10px;top:6px}

/* filters */
.filter-panel{position:absolute;left:0;top:184px;width:1200px;height:256px;background:var(--white);box-shadow:0 6px 10px rgba(0,0,0,.15);border-top:1px solid #ccc}
.filter-col{position:absolute;top:36px}
.filter-col h3{font-size:21px;font-weight:400;color:var(--ink);margin-bottom:12px;border-bottom:1px solid var(--line);padding-bottom:4px;width:140px}
.filter-col ul{list-style:none;font-size:15px;line-height:25px;color:#444}
.filter-col.double ul{columns:2;column-gap:40px;width:320px}

/* content */
.page-title{position:absolute;left:45px;top:460px;font-size:31px;color:var(--ink);font-weight:400}
.page-title b{color:var(--green);font-weight:400}
.section-title{position:absolute;left:75px;font-size:21px;color:#444;font-weight:400;display:flex;align-items:center;width:1080px}
.section-title::after{content:"";flex:1;height:1px;background:var(--line);margin-left:20px}
.card-row{position:absolute;left:55px;display:flex;gap:45px}
.card{position:relative;width:335px;height:675px;background:linear-gradient(180deg,#fafafa,#ececec);border:1px solid #ddd;border-radius:6px;box-shadow:0 2px 6px rgba(0,0,0,.12);padding:0 18px}
.ribbon{position:absolute;left:28px;right:28px;top:-6px;height:36px;background:linear-gradient(180deg,var(--green-light),var(--green));color:var(--white);font-size:17px;text-align:center;line-height:36px;border-radius:3px 3px 0 0}
.ribbon::before,.ribbon::after{content:"";position:absolute;top:0;border:6px solid transparent;border-bottom-color:var(--green-dark)}
.ribbon::before{left:-12px}
.ribbon::after{right:-12px}
.card-image{margin-top:30px;height:220px;border:1px solid #bbb}
.card h2{font-size:23px;font-weight:600;color:var(--ink);margin:16px 0 8px}
.card p{font-size:13.5px;line-height:19.5px;text-align:justify;color:#666;height:196px;overflow:hidden}
.share{display:flex;gap:8px;margin-top:12px}
.share i{width:18px;height:18px;border-radius:3px;background:#555;display:block}
.share i:nth-child(2){background:#5aa9d6}
.share i:nth-child(3){background:#3d5a96}
.meta{font-size:15px;color:var(--ink);margin-top:8px;line-height:25px;font-weight:600}
.meta .place{display:flex;align-items:center;gap:6px}
.progress{margin-top:8px;height:24px;background:var(--bar);border-radius:12px;overflow:hidden}
.progress span{display:block;width:55%;height:24px;background:linear-gradient(180deg,var(--green-light),var(--green));font-size:13px;line-height:24px;padding-left:16px;color:var(--ink);border-radius:12px 0 0 12px}
.see-more{position:absolute;right:50px;font-size:16px;color:var(--green);display:flex;align-items:center;gap:10px}

.pagination{position:absolute;right:50px;top:2176px;font-size:16px;color:var(--ink);font-weight:600;word-spacing:6px}
.pagination .current{color:var(--green)}

/* footer */
.site-footer{position:absolute;left:0;top:2222px;width:1200px;height:186px;border-top:1px solid #ccc;background:var(--white)}
.footer-col{position:absolute;top:24px}
.footer-col h4{font-size:20px;font-weight:400;color:var(--ink);margin-bottom:8px}
.footer-col ul{list-style:none;font-size:15px;line-height:24px;color:#555}
.footer-col.cats ul{columns:3;column-gap:40px;width:500px}
.newsletter p{font-size:14px;color:#555}
.newsletter .email{margin-top:10px;width:270px;height:36px;background:#ddd;border:1px solid #bbb;font-size:14px;line-height:34px;padding-left:12px;color:#555}
.newsletter .subscribe{margin:12px 0 0 95px;width:100px;height:34px;background:linear-gradient(#fff,#ddd);border:1px solid #aaa;border-radius:4px;font-size:14px;text-align:center;line-height:32px;color:var(--ink)}
.bottom-bar{position:absolute;left:0;top:2408px;width:1200px;height:63px;background:linear-gradient(#e6e6e6,#cfcfcf);display:flex;align-items:center;padding:0 45px;font-size:13px;color:#666}
.bottom-bar nav{margin-left:30px;display:flex;gap:22px;font-style:italic}
.bottom-bar .social{margin-left:auto;display:flex;gap:20px}
.bottom-bar .social i{width:38px;height:38px;border-radius:6px;display:block}
</style>
</head>
<body>

<header class="site-header">
  <div class="logo">LOGO GOES HERE</div>
  <div class="account-links">Register<span>|</span>Login</div>
  <div class="utility-links"><a>Blog</a><a>FAQ</a><a>Company</a></div>
  <div class="header-social"><i></i><i></i></div>
</header>

<nav class="main-nav">
  <ul><li class="active">Features</li><li>Browse</li><li>My Account</li><li>Portfolio</li></ul>
  <div class="search-box">Search
    <svg width="20" height="20" viewBox="0 0 20 20"><circle cx="8" cy="8" r="6" fill="none" stroke="#555" stroke-width="2"/><line x1="12.5" y1="12.5" x2="18" y2="18" stroke="#555" stroke-width="2.5"/></svg>
  </div>
</nav>

<section class="filter-panel">
  <div class="filter-col double" style="left:45px"><h3>Categories</h3>
    <ul><li>Category 1 name</li><li>Category 2 name</li><li>Category 3 name</li><li>Category 4 name</li><li>Category 7 name</li><li>Category 8 name</li><li>Category 5 name</li><li>Category 6 name</li><li>Category 9 name</li><li>Category 10 name</li><li>Category 11 name</li><li>Category 12 name</li></ul></div>
  <div class="filter-col" style="left:410px"><h3>Featured</h3>
    <ul><li>Recommended</li><li>Popular</li><li>Recently Launched</li><li>Ending Soon</li><li>Small Projects</li><li>Most Funded</li></ul></div>
  <div class="filter-col double" style="left:615px"><h3>Locations</h3>
    <ul><li>New York</li><li>Los Angeles</li><li>Brooklyn</li><li>Chicago</li><li>San Francisco</li><li>Portland</li><li>Seattle</li><li>Austin</li><li>New York</li><li>Boston</li><li>San Francisco</li><li>Chicago</li></ul></div>
  <div class="filter-col" style="left:990px"><h3>Sort By</h3>
    <ul><li>Recommended</li><li>Popular</li><li>Recently Launched</li><li>Ending Soon</li><li>Small Projects</li><li>Most Funded</li></ul></div>
</section>

<h1 class="page-title"><b>Design</b> / Graphic Design</h1>

<h2 class="section-title" style="top:516px">Popular This Week</h2>
<div class="card-row" style="top:584px">
  <article class="card"><div class="ribbon">New &amp; Noteworthy</div>
    <div class="card-image" role="img" aria-label="Project photo: large statue bust in a gallery" style="background:linear-gradient(160deg,#b9c0c4,#4a5a50 60%,#2b332e)"></div>
    <h2>Project Title Will Be Here</h2>
    <p>Lorem ipsum dolor sit amet, consectetur adipisicing elit, sed do eiusmod tempor incididunt ut labore et dolore magna aliqua. Ut enim ad minim veniam, quis nostrud exercitation ullamco laboris nisi ut aliquip ex ea commodo consequat. Duis aute irure dolor in reprehenderit in voluptate velit esse cillum dolore eu fugiat nulla pariatur. Excepteur sint occaecat cupidatat non proident, sunt in culpa qui officia deserunt mollit anim id. Excepteur sint occaecat cupidatat non proident</p>
    <div class="share"><i></i><i></i><i></i></div>
    <div class="meta"><div class="place"><svg width="12" height="16" viewBox="0 0 12 16"><path d="M6 0a6 6 0 0 0-6 6c0 4.5 6 10 6 10s6-5.5 6-10a6 6 0 0 0-6-6zm0 8.5a2.5 2.5 0 1 1 0-5 2.5 2.5 0 0 1 0 5z" fill="#222"/></svg>Vancouver, B.C, Canada</div><div>8 days left</div><div>Funded $65,000 of $100,000</div></div>
    <div class="progress"><span>65%</span></div>
  </article>
  <article class="card"><div class="ribbon">Popular</div>
    <div class="card-image" role="img" aria-label="Project photo: man in a powered wheelchair on a street" style="background:linear-gradient(180deg,#8d9196,#5b5f63 50%,#2d2f31)"></div>
    <h2>Project Title Will Be Here</h2>
    <p>Lorem ipsum dolor sit amet, consectetur adipisicing elit, sed do eiusmod tempor incididunt ut labore et dolore magna aliqua. Ut enim ad minim veniam, quis nostrud exercitation ullamco laboris nisi ut aliquip ex ea commodo consequat. Duis aute irure dolor in reprehenderit in voluptate velit esse cillum dolore eu fugiat nulla pariatur. Excepteur sint occaecat cupidatat non proident, sunt in culpa qui officia deserunt mollit anim id. Excepteur sint occaecat cupidatat non proident</p>
    <div class="share"><i></i><i></i><i></i></div>
    <div class="meta"><div class="place"><svg width="12" height="16" viewBox="0 0 12 16"><path d="M6 0a6 6 0 0 0-6 6c0 4.5 6 10 6 10s6-5.5 6-10a6 6 0 0 0-6-6zm0 8.5a2.5 2.5 0 1 1 0-5 2.5 2.5 0 0 1 0 5z" fill="#222"/></svg>Vancouver, B.C, Canada</div><div>8 days left</div><div>Funded $65,000 of $100,000</div></div>
    <div class="progress"><span>65%</span></div>
  </article>
  <article class="card"><div class="ribbon">Closing Soon</div>
    <div class="card-image" role="img" aria-label="Project illustration: cartoon jungle animals with sticker app title" style="background:linear-gradient(160deg,#6fbf3a,#e8b52a 55%,#3f8a1c)"></div>
    <h2>Project Title Will Be Here</h2>
    <p>Lorem ipsum dolor sit amet, consectetur adipisicing elit, sed do eiusmod tempor incididunt ut labore et dolore magna aliqua. Ut enim ad minim veniam, quis nostrud exercitation ullamco laboris nisi ut aliquip ex ea commodo consequat. Duis aute irure dolor in reprehenderit in voluptate velit esse cillum dolore eu fugiat nulla pariatur. Excepteur sint occaecat cupidatat non proident, sunt in culpa qui officia deserunt mollit anim id. Excepteur sint occaecat cupidatat non proident</p>
    <div class="share"><i></i><i></i><i></i></div>
    <div class="meta"><div class="place"><svg width="12" height="16" viewBox="0 0 12 16"><path d="M6 0a6 6 0 0 0-6 6c0 4.5 6 10 6 10s6-5.5 6-10a6 6 0 0 0-6-6zm0 8.5a2.5 2.5 0 1 1 0-5 2.5 2.5 0 0 1 0 5z" fill="#222"/></svg>Vancouver, B.C, Canada</div><div>8 days left</div><div>Funded $65,000 of $100,000</div></div>
    <div class="progress"><span>65%</span></div>
  </article>
</div>
<a class="see-more" style="top:1298px"><svg width="26" height="12" viewBox="0 0 26 12"><path d="M0 6h22M17 1l6 5-6 5" fill="none" stroke="#6cae1c" stroke-width="2"/></svg>See more popular projects</a>

<h2 class="section-title" style="top:1328px">Recently Successful</h2>
<div class="card-row" style="top:1392px">
  <article class="card"><div class="ribbon">New &amp; Noteworthy</div>
    <div class="card-image" role="img" aria-label="Project illustration: comic festival poster" style="background:linear-gradient(150deg,#f08a1c,#3a7ab8 60%,#1d3e6a)"></div>
    <h2>Project Title Will Be Here</h2>
    <p>Lorem ipsum dolor sit amet, consectetur adipisicing elit, sed do eiusmod tempor incididunt ut labore et dolore magna aliqua. Ut enim ad minim veniam, quis nostrud exercitation ullamco laboris nisi ut aliquip ex ea commodo consequat. Duis aute irure dolor in reprehenderit in voluptate velit esse cillum dolore eu fugiat nulla pariatur. Excepteur sint occaecat cupidatat non proident, sunt in culpa qui officia deserunt mollit anim id. Excepteur sint occaecat cupidatat non proident</p>
    <div class="share"><i></i><i></i><i></i></div>
    <div class="meta"><div class="place"><svg width="12" height="16" viewBox="0 0 12 16"><path d="M6 0a6 6 0 0 0-6 6c0 4.5 6 10 6 10s6-5.5 6-10a6 6 0 0 0-6-6zm0 8.5a2.5 2.5 0 1 1 0-5 2.5 2.5 0 0 1 0 5z" fill="#222"/></svg>Vancouver, B.C, Canada</div><div>8 days left</div><div>Funded $65,000 of $100,000</div></div>
    <div class="progress"><span>65%</span></div>
  </article>
  <article class="card"><div class="ribbon">Closing Soon</div>
    <div class="card-image" role="img" aria-label="Project artwork: glowing green sci-fi orb on dark background" style="background:radial-gradient(circle at 50% 55%,#9be04a,#2f5e12 35%,#0c140a 70%)"></div>
    <h2>Project Title Will Be Here</h2>
    <p>Lorem ipsum dolor sit amet, consectetur adipisicing elit, sed do eiusmod tempor incididunt ut labore et dolore magna aliqua. Ut enim ad minim veniam, quis nostrud exercitation ullamco laboris nisi ut aliquip ex ea commodo consequat. Duis aute irure dolor in reprehenderit in voluptate velit esse cillum dolore eu fugiat nulla pariatur. Excepteur sint occaecat cupidatat non proident, sunt in culpa qui officia deserunt mollit anim id. Excepteur sint occaecat cupidatat non proident</p>
    <div class="share"><i></i><i></i><i></i></div>
    <div class="meta"><div class="place"><svg width="12" height="16" viewBox="0 0 12 16"><path d="M6 0a6 6 0 0 0-6 6c0 4.5 6 10 6 10s6-5.5 6-10a6 6 0 0 0-6-6zm0 8.5a2.5 2.5 0 1 1 0-5 2.5 2.5 0 0 1 0 5z" fill="#222"/></svg>Vancouver, B.C, Canada</div><div>8 days left</div><div>Funded $65,000 of $100,000</div></div>
    <div class="progress"><span>65%</span></div>
  </article>
  <article class="card"><div class="ribbon">Popular</div>
    <div class="card-image" role="img" aria-label="Project illustration: white horse leaping across a night sky" style="background:radial-gradient(circle at 50% 45%,#cfe3ff,#3a66c4 45%,#0e1f5a)"></div>
    <h2>Project Title Will Be Here</h2>
    <p>Lorem ipsum dolor sit amet, consectetur adipisicing elit, sed do eiusmod tempor incididunt ut labore et dolore magna aliqua. Ut enim ad minim veniam, quis nostrud exercitation ullamco laboris nisi ut aliquip ex ea commodo consequat. Duis aute irure dolor in reprehenderit in voluptate velit esse cillum dolore eu fugiat nulla pariatur. Excepteur sint occaecat cupidatat non proident, sunt in culpa qui officia deserunt mollit anim id. Excepteur sint occaecat cupidatat non proident</p>
    <div class="share"><i></i><i></i><i></i></div>
    <div class="meta"><div class="place"><svg width="12" height="16" viewBox="0 0 12 16"><path d="M6 0a6 6 0 0 0-6 6c0 4.5 6 10 6 10s6-5.5 6-10a6 6 0 0 0-6-6zm0 8.5a2.5 2.5 0 1 1 0-5 2.5 2.5 0 0 1 0 5z" fill="#222"/></svg>Vancouver, B.C, Canada</div><div>8 days left</div><div>Funded $65,000 of $100,000</div></div>
    <div class="progress"><span>65%</span></div>
  </article>
</div>
<a class="see-more" style="top:2108px"><svg width="26" height="12" viewBox="0 0 26 12"><path d="M0 6h22M17 1l6 5-6 5" fill="none" stroke="#6cae1c" stroke-width="2"/></svg>See more successful projects</a>

<div class="pagination">Result Pages : |&lt; &lt; 1 <span class="current">2</span> 3 .... 10 11 12 &gt; &gt;|</div>

<footer class="site-footer">
  <div class="footer-col" style="left:45px"><h4>Common Links</h4>
    <ul><li>My Account</li><li>Blog</li><li>Company</li><li>FAQ</li></ul></div>
  <div class="footer-col cats" style="left:300px"><h4>Categories</h4>
    <ul><li>Category 1 name</li><li>Category 2 name</li><li>Category 3 name</li><li>Category 4 name</li><li>Category 5 name</li><li>Category 6 name</li><li>Category 7 name</li><li>Category 8 name</li><li>Category 9 name</li><li>Category 10 name</li><li>Category 11 name</li><li>Category 12 name</li></ul></div>
  <div class="footer-col newsletter" style="left:845px"><h4>Newsletter</h4>
    <p>Subscribe to our newsletter for updates</p>
    <div class="email">Your email</div>
    <div class="subscribe">Subscribe</div></div>
</footer>

<div class="bottom-bar">
  <span>Copyright 2011 Company INC.</span>
  <nav><a>Terms of Use</a><a>Privacy Policy</a><a>Contact Us</a></nav>
  <div class="social">
    <i style="background:#c62a1e"></i><i style="background:#3d8fd0"></i><i style="background:#3b5a98"></i><i style="background:#f2891d"></i><i style="background:#4fb8e6"></i>
  </div>
</div>

</body>
</html>
```